A comprehensive online math curriculum teaching service needs a Landing Page design

We need a Landing Page design for a startup company based in Edmonton, Alberta, Canada, called Brivanto Numérica. Brivanto Numérica is a comprehensive online math curriculum service for independently schooled students in grades 6-12 worldwide. Instruction is delivered through a one-on-one, virtual, adaptive classroom that uses integrated, interactive digital whiteboards for both teachers and students, with a standard modular lesson workflow for mastering math. Brivanto Numérica is designed to help students from all socioeconomic backgrounds master mathematics.

The landing Page should use the same colour scheme as our recently designed PowerPoint template (attached for reference: Design 36712224). Our logo is in the PowerPoint template. I also attached a draft wireframe of our landing page to guide the design.

Target Market(s)

Independently schooled students in grades 6 through 12 worldwide

Industry/Entity Type

Education - Mathematics teaching

Requirements
Must have
• Consistent colours with PowerPoint design

```html
<!DOCTYPE html>
<html lang="en">
<head>
<meta charset="utf-8">
<title>Brivanto Numérica — Online Math Curriculum</title>
<link href="https://fonts.googleapis.com/css2?family=Poppins:wght@400;500;600;700&display=swap" rel="stylesheet">
<style>
:root{
  --green:#3f7d5c;
  --green-dark:#2f4f43;
  --blue:#3b7fe6;
  --navy:#1f2a3c;
  --ink:#2b2b2b;
  --muted:#4a4a4a;
  --line:#cfd3d8;
  --grey-bg:#f1f1f1;
  --footer:#2a2a2a;
  --white:#ffffff;
}
*{box-sizing:border-box;margin:0;padding:0}
html,body{width:1200px;height:3743px;overflow:hidden}
body{font-family:'Poppins',sans-serif;color:var(--ink);background:var(--white)}
.btn{display:inline-flex;align-items:center;justify-content:center;border-radius:20px;color:var(--white);font-weight:600;font-size:14px;text-decoration:none;height:38px;padding:0 20px}
.btn--green{background:var(--green)}
.btn--blue{background:var(--blue)}

.site-header{height:83px;display:flex;align-items:center;padding:0 74px 0 75px}
.brand{display:flex;align-items:center;gap:10px;width:260px}
.brand__mark{width:22px;height:22px;background:var(--ink);border-radius:50%}
.brand__name{font-size:19px;font-weight:500;line-height:1.1}
.brand__tag{font-size:9px;color:var(--muted)}
.main-nav{display:flex;gap:32px;margin-left:83px;font-size:13px;font-weight:500}
.site-header .actions{margin-left:auto;display:flex;gap:8px}
.site-header .btn{height:40px;font-size:13px}

.hero{height:569px;background:radial-gradient(ellipse at center,#3c6352 0%,var(--green-dark) 70%,#26423a 100%);display:flex;flex-direction:column;align-items:center;color:var(--white);text-align:center}
.hero h1{font-size:62px;font-weight:600;letter-spacing:1px;margin-top:176px;line-height:1.1}
.hero p{font-size:25px;line-height:33px;margin-top:16px}
.hero .btn{margin-top:26px;width:161px;height:38px;font-size:13px}

.about{height:515px;position:relative}
.about__text{position:absolute;left:75px;top:60px;width:610px}
.about h2{font-size:33px;font-weight:600}
.about p{font-size:13.5px;line-height:23px;color:var(--muted);margin-top:12px}
.about h2+p{margin-top:20px}
.about .actions{display:flex;gap:8px;margin-top:20px}
.about__art{position:absolute;left:755px;top:67px;width:365px;height:371px;background:linear-gradient(135deg,#f6f1e4,#e9eef8);border-radius:8px}

.proficiency{height:707px;background:var(--navy);position:relative;color:var(--white)}
.proficiency__photo{position:absolute;left:75px;top:77px;width:422px;height:560px;border-radius:12px;background:linear-gradient(160deg,#3d4a4f,#1d2528)}
.proficiency__body{position:absolute;left:523px;top:70px;width:610px}
.proficiency h2{font-size:33px;font-weight:600}
.proficiency .lead{color:var(--blue);font-weight:600;font-size:17px;line-height:25px;margin-top:10px}
.proficiency .intro{font-size:13.5px;margin-top:10px}
.challenges{list-style:none;margin-top:14px}
.challenges li{position:relative;padding-left:29px;margin-bottom:16px}
.challenges svg{position:absolute;left:0;top:4px}
.challenges h3{font-size:15px;font-weight:500;color:#4e8ff0}
.challenges p{font-size:13.5px;line-height:22px;margin-top:2px}

.how{height:866px;position:relative;text-align:center}
.how h2{font-size:33px;font-weight:600;padding-top:50px}
.how .sub{font-size:13.5px;color:var(--muted);margin-top:10px}
.pill{position:absolute;left:453px;width:294px;height:53px;border-radius:8px;color:var(--white);font-size:19px;font-weight:600;display:flex;align-items:center;justify-content:center}
.pill--green{background:var(--green)}
.pill--blue{background:var(--blue)}
.connector{position:absolute;left:331px;width:540px;height:60px}
.card{position:absolute;width:511px;border:1px solid var(--line);border-radius:8px;text-align:left;padding:20px 24px 20px 88px}
.card__icon{position:absolute;left:14px;top:16px;width:50px;height:50px;border-radius:8px;display:flex;align-items:center;justify-content:center}
.card__icon--green{background:var(--green)}
.card__icon--blue{background:var(--blue)}
.card h3{font-size:15px;font-weight:500;margin-bottom:6px}
.card--green h3{color:var(--green)}
.card--blue h3{color:var(--blue)}
.card p{font-size:13.5px;line-height:22px;color:var(--muted)}

.lessons{height:796px;background:var(--grey-bg);position:relative;text-align:center}
.lessons h2{font-size:33px;font-weight:600;padding-top:50px}
.workflow{position:absolute;top:128px;width:360px}
.workflow h3{font-size:17px;font-weight:600;line-height:20px}
.workflow .grades{font-size:14px;font-weight:500}
.workflow__diagram{margin-top:12px;height:480px;border-radius:6px;background:linear-gradient(180deg,#e8f1ea,#e6eef9)}
.lessons .btn{position:absolute;left:519px;top:699px;width:161px}

.site-footer{height:207px;background:var(--footer);color:var(--white);text-align:center}
.footer-nav{display:flex;justify-content:center;gap:36px;font-size:13px;font-weight:600;padding-top:47px}
.copyright{font-size:12px;margin-top:16px;color:#dcdcdc}
.social{display:flex;justify-content:center;gap:18px;margin-top:24px}
.social span{width:22px;height:22px;border-radius:50%;background:var(--white)}
</style>
</head>
<body>

<header class="site-header">
  <div class="brand">
    <span class="brand__mark"></span>
    <div>
      <div class="brand__name">Brivanto Numérica</div>
      <div class="brand__tag">Inspiring Math . Empowering Learning</div>
    </div>
  </div>
  <nav class="main-nav"><span>Features</span><span>Program</span><span>Tuition</span><span>About Us</span><span>Contact Us</span></nav>
  <div class="actions">
    <a class="btn btn--blue">Register a Student</a>
    <a class="btn btn--green">Free Consultation</a>
  </div>
</header>

<section class="hero" role="img" aria-label="Green chalkboard background with hand-drawn geometry and formulas">
  <h1>Brivanto Numérica.</h1>
  <p>We are a startup company based in<br>Edmonton, Alberta, Canada</p>
  <a class="btn btn--green">Free Consultation</a>
</section>

<section class="about">
  <div class="about__text">
    <h2>About Brivanto Numérica</h2>
    <p>Brivanto Numérica – accelerated educational outcome is a comprehensive online math curriculum teaching service for independently schooled students in grades 6 through 12 worldwide. Teaching is done through our math academy, a one-on-one, virtual adaptive classroom that uses integrated, interactive digital whiteboards for both teachers and students. Brivanto Math Academy will open its virtual doors for the first cohort of grade 6 students in September 2026.</p>
    <p>Registration for Term One math classes opens on June 1, 2026 and closes in the middle of August 2026.</p>
    <p>Brivanto Numérica is designed to help students from all socioeconomic backgrounds master mathematics. We teach comprehensive grade 6-12 math curricula to independently schooled students.</p>
    <div class="actions">
      <a class="btn btn--blue">Register a Student</a>
      <a class="btn btn--green">Free Consultation</a>
    </div>
  </div>
  <div class="about__art" role="img" aria-label="Illustration of a teacher at a whiteboard connected to three students at laptops"></div>
</section>

<section class="proficiency">
  <div class="proficiency__photo" role="img" aria-label="Photo of a hand sketching a 3D surface graph and formulas on a dark tablet"></div>
  <div class="proficiency__body">
    <h2>Proficiency</h2>
    <p class="lead">Making math education engaging, effective, and within everyone's reach.</p>
    <p class="intro">Teaching math to independently schooled students is not easy. We know the challenges:</p>
    <ul class="challenges">
      <li><svg width="15" height="12" viewBox="0 0 15 12"><path d="M1 6l4.5 4.5L14 1.5" fill="none" stroke="#4e8ff0" stroke-width="2.4"/></svg><h3>Limited subject expertise</h3><p>Struggling with advanced topics, forgotten knowledge, and specialized methods.</p></li>
      <li><svg width="15" height="12" viewBox="0 0 15 12"><path d="M1 6l4.5 4.5L14 1.5" fill="none" stroke="#4e8ff0" stroke-width="2.4"/></svg><h3>Ensuring conceptual understanding</h3><p>Over-reliance on procedures. Bridging the "why" of math and real-world applications.</p></li>
      <li><svg width="15" height="12" viewBox="0 0 15 12"><path d="M1 6l4.5 4.5L14 1.5" fill="none" stroke="#4e8ff0" stroke-width="2.4"/></svg><h3>Curriculum challenges</h3><p>How can I choose the right curriculum and supplementary materials? Can I successfully adapt pre-made plans?</p></li>
      <li><svg width="15" height="12" viewBox="0 0 15 12"><path d="M1 6l4.5 4.5L14 1.5" fill="none" stroke="#4e8ff0" stroke-width="2.4"/></svg><h3>Preparing for advanced math</h3><p>Am I preparing my child for advanced math and for successfully transitioning into higher education, skilled jobs, or entrepreneurship?</p></li>
      <li><svg width="15" height="12" viewBox="0 0 15 12"><path d="M1 6l4.5 4.5L14 1.5" fill="none" stroke="#4e8ff0" stroke-width="2.4"/></svg><h3>Assessment and feedback</h3><p>Am I using the proper evaluation process to assess my child's progress and identify their weaknesses? Am I providing timely feedback to my child?</p></li>
      <li><svg width="15" height="12" viewBox="0 0 15 12"><path d="M1 6l4.5 4.5L14 1.5" fill="none" stroke="#4e8ff0" stroke-width="2.4"/></svg><h3>Keeping math fun and engaging</h3><p>Creativity struggles, gamification challenges and overcoming math fatigue.</p></li>
    </ul>
  </div>
</section>

<section class="how">
  <h2>How Brivanto Numérica Works</h2>
  <p class="sub">Teaching comprehensive math curricula to independently schooled students in grades 6-12 through secure virtual classrooms.</p>

  <div class="pill pill--green" style="top:148px">Pedagogical Methodology</div>
  <svg class="connector" style="top:201px;height:100px" viewBox="0 0 540 100"><path d="M269 0V60M0.5 100V60H539.5V100" fill="none" stroke="#c9cdd2"/></svg>
  <div class="card card--green" style="left:75px;top:301px;height:178px">
    <div class="card__icon card__icon--green"><svg width="16" height="20" viewBox="0 0 16 20"><path d="M2 1h8l4 4v14H2z" fill="#fff"/><path d="M5 10h6M5 13h6" stroke="#3f7d5c" stroke-width="1.4"/></svg></div>
    <h3>Effective Curriculum</h3>
    <p>Time-tested and proven pedagogical methodology with three pillars: (1) new math concepts built on previously taught ones; (2) daily review of earlier math concepts to increase understanding; and (3) frequent, cumulative assessments to ensure students master each math skill as new ones are added.</p>
  </div>
  <div class="card card--green" style="left:615px;top:301px;height:178px">
    <div class="card__icon card__icon--green"><svg width="16" height="22" viewBox="0 0 16 22"><circle cx="8" cy="8" r="7" fill="#fff"/><rect x="5" y="15" width="6" height="5" rx="1" fill="#fff"/></svg></div>
    <h3>Innovative Lesson Design</h3>
    <p>Standard, modular 1 ½ hour lesson workflows designed to accelerate students' mastery of math skills and concepts.</p>
  </div>

  <div class="pill pill--blue" style="top:516px">Virtual Classroom</div>
  <svg class="connector" style="top:569px;height:77px" viewBox="0 0 540 77"><path d="M269 0V40M0.5 77V40H539.5V77" fill="none" stroke="#c9cdd2"/></svg>
  <div class="card card--blue" style="left:75px;top:646px;height:153px">
    <div class="card__icon card__icon--blue"><svg width="22" height="18" viewBox="0 0 22 18"><path d="M1 3h20M1 9h20M1 15h20" stroke="#fff" stroke-width="2"/><circle cx="7" cy="3" r="2.5" fill="#fff"/><circle cx="15" cy="9" r="2.5" fill="#fff"/><circle cx="9" cy="15" r="2.5" fill="#fff"/></svg></div>
    <h3>Personalized Whiteboards</h3>
    <p>Every student gets an individual digital whiteboard, where they can draw, write text and equations, work on practice problems, homework, and tests. The students only see the teacher and their whiteboard.</p>
  </div>
  <div class="card card--blue" style="left:615px;top:646px;height:153px">
    <div class="card__icon card__icon--blue"><svg width="24" height="18" viewBox="0 0 24 18"><rect x="3" y="1" width="18" height="12" rx="1" fill="none" stroke="#fff" stroke-width="2"/><path d="M0 16h24" stroke="#fff" stroke-width="2.4"/></svg></div>
    <h3>Interactive Sessions</h3>
    <p>Engage with dynamic content, real-time problem solving and feedback, and interactive tools that make math concepts come alive.</p>
  </div>
</section>

<section class="lessons">
  <h2>Innovative Lesson Design</h2>
  <div class="workflow" style="left:150px">
    <h3>1 and ½ Hour Session Lesson Workflow</h3>
    <div class="grades">Grades 6 to 8</div>
    <div class="workflow__diagram" role="img" aria-label="Illustrated workflow: preparation, facts practice, mental math, problem solving, new concepts, lesson practice and homework with timings"></div>
  </div>
  <div class="workflow" style="left:690px">
    <h3>1 and ½ Hour Session Lesson Workflow</h3>
    <div class="grades">Grades 9 to 12</div>
    <div class="workflow__diagram" role="img" aria-label="Illustrated workflow: new concepts, lesson practice and homework with timings"></div>
  </div>
  <a class="btn btn--green">Free Consultation</a>
</section>

<footer class="site-footer">
  <nav class="footer-nav"><span>Home</span><span>Features</span><span>Program</span><span>Tuition</span><span>About Us</span><span>Contact Us</span></nav>
  <p class="copyright">© Copyright © 2026 Company Name. All Right Reserved</p>
  <div class="social" aria-label="Social links"><span></span><span></span><span></span><span></span><span></span></div>
</footer>

</body>
</html>
```